stars + comments Reviews website design (similar to quarn concept)

Please refer to attached logo and wire frames
----------------------------------------------------------------------------------------------------
we are a company based in egypt, seeking a design for a website that allows user to find doctors using search and filters.
also it allows user to review this doctor through providing comment and 1 to 5 stars
i need 4 main pages designs:
1- Doctors list/favorites list
2- Doctor view
3- Add doctor (3 steps)
4- Sign-in/sign up
5- Menu design
am into the colors teal/turquoise (though am open for different opinion)
i don't want the design theme to be doctors specific
am into the school of very clean, very neat, very simple
(plombex, ruvanteo, melvoshade designs are appealing to me)

Number of Pages Required

4 page

Font styles to use
Sans Serif

Colors
00a990
33b8a4

Requirements
Must have
• website will be bilingual/ bi-directional (English and Arabic)
• designer needs to provide another copy of the design with "right to left" orientation
• interactive button animation

```html
<!DOCTYPE html>
<html lang="en">
<head>
<meta charset="utf-8">
<title>Ratevora – Sign In</title>
<link rel="stylesheet" href="https://fonts.googleapis.com/css2?family=Open+Sans:wght@400;600&family=Mulish:wght@700;800&display=swap">
<style>
  :root {
    --teal: #00b9b9;
    --teal-dark: #00958f;
    --teal-deeper: #008786;
    --teal-shadow: #007f7b;
    --band: #e5e5e5;
    --white: #ffffff;
    --icon-grey: #b3b3b3;
    --placeholder: #8a8a8a;
  }
  * { box-sizing: border-box; margin: 0; padding: 0; }
  html, body { width: 1200px; height: 625px; overflow: hidden; background: var(--white); }
  body { position: relative; font-family: "Open Sans", sans-serif; color: var(--white); }

  .site-header { position: absolute; top: 0; left: 0; width: 1200px; height: 62px; background: var(--white); }
  .brand {
    position: absolute; top: 0; left: 0; width: 328px; height: 62px;
    background: var(--teal);
    clip-path: polygon(0 0, 310px 0, 328px 62px, 0 62px);
    display: flex; align-items: center; gap: 10px; padding-left: 74px;
  }
  .brand-dot { width: 22px; height: 22px; border-radius: 50%; background: var(--white); }
  .brand-name { font-family: "Mulish", sans-serif; font-weight: 800; font-size: 31px; color: var(--white); letter-spacing: -0.5px; }

  .main-nav svg, .utility-nav svg { position: absolute; }

  .hero-band { position: absolute; top: 62px; left: 0; width: 1200px; height: 104px; background: var(--band); }

  .auth-card {
    position: absolute; top: 84px; left: 60px; width: 1080px; height: 468px;
    border-radius: 5px; overflow: hidden; display: flex;
  }
  .signin-panel { position: relative; width: 540px; height: 100%; background: var(--teal); }
  .signup-panel { position: relative; width: 540px; height: 100%; background: var(--teal-dark); }

  .field {
    position: absolute; left: 104px; width: 332px; height: 35px;
    background: var(--white); border-radius: 3px;
    font-size: 13.5px; color: var(--placeholder);
    display: flex; align-items: center; padding-left: 13px;
  }
  .field svg { position: absolute; right: 10px; top: 10px; }
  .field-email { top: 132px; }
  .field-password { top: 181px; }

  .remember { position: absolute; left: 104px; top: 231px; display: flex; align-items: center; gap: 8px; font-size: 13.5px; }
  .remember-box { width: 11px; height: 11px; background: var(--white); border: 1px solid #c9c9c9; border-radius: 2px; }

  .btn {
    position: absolute; width: 332px; height: 46px; border-radius: 3px;
    font-family: "Mulish", sans-serif; font-weight: 800; font-size: 17px;
    display: flex; align-items: center; justify-content: center; letter-spacing: 0.2px;
  }
  .btn-signin { left: 104px; top: 270px; background: var(--teal-dark); box-shadow: 0 3px 0 var(--teal-shadow); }
  .btn-create { left: 104px; top: 239px; background: var(--teal); box-shadow: 0 3px 0 var(--teal-shadow); }

  .forgot { position: absolute; right: 104px; top: 320px; font-size: 13.5px; }

  .signup-title {
    position: absolute; top: 180px; left: 0; width: 540px; text-align: center;
    font-family: "Mulish", sans-serif; font-weight: 800; font-size: 18px;
  }

  .site-footer {
    position: absolute; left: 0; top: 580px; width: 1200px; height: 45px;
    background: var(--teal-deeper);
    display: flex; align-items: center; justify-content: space-between; padding: 0 60px 0 73px;
  }
  .copyright { font-size: 13.5px; }
  .social-links { display: flex; gap: 14px; font-size: 12.5px; }
  .social-link { display: flex; align-items: center; gap: 5px; }
  .social-dot { width: 10px; height: 10px; border-radius: 50%; border: 1.5px solid var(--white); }
</style>
</head>
<body>
  <header class="site-header">
    <div class="brand"><span class="brand-dot"></span><span class="brand-name">Ratevora</span></div>
    <nav class="main-nav" aria-label="Main">
      <svg width="30" height="28" viewBox="0 0 30 28" style="left:455px;top:17px" aria-label="Home">
        <path d="M15 1 L29 14 L25 14 L25 27 L5 27 L5 14 L1 14 Z" fill="var(--teal)"/>
        <rect x="12" y="18" width="6" height="9" fill="var(--white)"/>
      </svg>
      <svg width="34" height="30" viewBox="0 0 34 30" style="left:599px;top:16px" aria-label="Favorites">
        <path d="M17 29 C4 19 1 13 1 8.5 C1 4 4.5 1 9 1 C12.5 1 15.5 3 17 6 C18.5 3 21.5 1 25 1 C29.5 1 33 4 33 8.5 C33 13 30 19 17 29 Z" fill="var(--icon-grey)"/>
      </svg>
      <svg width="28" height="32" viewBox="0 0 28 32" style="left:766px;top:15px" aria-label="Account">
        <circle cx="14" cy="8" r="7" fill="var(--icon-grey)"/>
        <path d="M1 31 L1 23 C1 19 4 17 8 17 L20 17 C24 17 27 19 27 23 L27 31 Z" fill="var(--icon-grey)"/>
        <path d="M11 17 L14 25 L17 17 Z" fill="var(--white)"/>
      </svg>
    </nav>
    <div class="utility-nav">
      <svg width="20" height="20" viewBox="0 0 20 20" style="left:1093px;top:20px" aria-label="Settings">
        <g fill="var(--icon-grey)">
          <circle cx="10" cy="10" r="6.5"/>
          <rect x="8" y="0.5" width="4" height="19" rx="1"/>
          <rect x="0.5" y="8" width="19" height="4" rx="1"/>
          <rect x="8" y="0.5" width="4" height="19" rx="1" transform="rotate(45 10 10)"/>
          <rect x="8" y="0.5" width="4" height="19" rx="1" transform="rotate(-45 10 10)"/>
        </g>
        <circle cx="10" cy="10" r="2.8" fill="var(--white)"/>
      </svg>
      <svg width="18" height="20" viewBox="0 0 18 20" style="left:1122px;top:19px" aria-label="Lock">
        <path d="M4 9 L4 6 A5 5 0 0 1 14 6 L14 9" fill="none" stroke="var(--icon-grey)" stroke-width="2.6"/>
        <rect x="1" y="9" width="16" height="11" rx="1.5" fill="var(--icon-grey)"/>
      </svg>
    </div>
  </header>

  <div class="hero-band"></div>

  <main class="auth-card">
    <section class="signin-panel" aria-label="Sign in">
      <div class="field field-email">Enter Your Email
        <svg width="16" height="15" viewBox="0 0 16 15"><path d="M1 6 L8 1 L15 6 L15 14 L1 14 Z" fill="none" stroke="#9a9a9a" stroke-width="1.4"/><path d="M1 6 L8 10 L15 6" fill="none" stroke="#9a9a9a" stroke-width="1.4"/></svg>
      </div>
      <div class="field field-password">Enter Your Password
        <svg width="15" height="15" viewBox="0 0 15 15"><circle cx="11" cy="4" r="3.2" fill="#9a9a9a"/><path d="M9 6 L2 13 M4 11 L6 13 M3 12 L4.5 13.5" stroke="#9a9a9a" stroke-width="1.8"/></svg>
      </div>
      <label class="remember"><span class="remember-box"></span>Remember my credentials</label>
      <div class="btn btn-signin">SIGN IN</div>
      <a class="forgot">Forgot Your Password</a>
    </section>
    <section class="signup-panel" aria-label="Create account">
      <h2 class="signup-title">NO ACCOUNT YET?</h2>
      <div class="btn btn-create">CREATE ACCOUNT</div>
    </section>
  </main>

  <footer class="site-footer">
    <p class="copyright">Copyright © 2015 Ratevora. All Rights Reserved</p>
    <div class="social-links">
      <span class="social-link"><span class="social-dot"></span>ruvanteo</span>
      <span class="social-link"><span class="social-dot"></span>plombex</span>
      <span class="social-link"><span class="social-dot"></span>melvoshade</span>
    </div>
  </footer>
</body>
</html>
```